Snack package design "Lantern Curl Bites"

Looking to create a fun package design of snack. Snack is sweet and crunchy; great for people that wants to munch on stuff. Name of the Snack is "Lantern Curl Bites". The net weight should be 16oz (453 grams). I added brand "TWbR" Tiny Wonders bring Rain on the file. I also added picture of the snack. Package will be a pouch type.

Target Market(s)

People that like sweet snacks

Industry/Entity Type

Food snacks

Requirements
Must have
• Name of Snack "Lantern Curl Bites" and logo of company on top left.
Nice to have
• something that's simple and clean design

```html
<!DOCTYPE html>
<html lang="en">
<head>
<meta charset="utf-8">
<title>Lantern Curl Bites – Pouch Colourways</title>
<link rel="stylesheet" href="https://fonts.googleapis.com/css2?family=Bebas+Neue&family=Allura&family=Libre+Baskerville&family=Nunito:wght@700&display=swap">
<style>
  :root {
    --page: #ffffff;
    --ink-white: #f6f4f2;
    --band-gold: #e8a93a;
    --band-coral: #c8604c;
    --band-text: #5a3a20;
    --snack-light: #f0b45a;
    --snack-mid: #d98a3a;
    --snack-deep: #b8612a;
    --charcoal: #2b2a2a;
    --rose: #b05866;
    --forest: #24392f;
    --stone: #9d9d9d;
    --script-wine: #8e2f3a;
    --script-amber: #e2a53e;
    --script-red: #a8353b;
  }
  * { margin: 0; padding: 0; box-sizing: border-box; }
  html, body { width: 800px; height: 1200px; overflow: hidden; background: var(--page); }
  .sheet { position: relative; width: 800px; height: 1200px; }

  .pouch {
    position: absolute;
    width: 324px;
    height: 528px;
    background: var(--pouch-colour);
    border-radius: 2px;
    overflow: hidden;
  }
  .pouch--charcoal { left: 36px;  top: 46px;  --pouch-colour: var(--charcoal); --script-colour: var(--script-wine); --band-colour: var(--band-gold); }
  .pouch--rose     { left: 441px; top: 46px;  --pouch-colour: var(--rose);     --script-colour: var(--script-amber); --band-colour: var(--band-gold); }
  .pouch--forest   { left: 36px;  top: 638px; --pouch-colour: var(--forest);   --script-colour: var(--script-wine); --band-colour: var(--band-gold); }
  .pouch--stone    { left: 441px; top: 638px; --pouch-colour: var(--stone);    --script-colour: var(--script-red);  --band-colour: var(--band-coral); }

  .pouch__seal {
    position: absolute; left: 0; right: 0; top: 88px;
    height: 1px; background: rgba(0,0,0,0.18);
  }
  .pouch__seal--upper { top: 46px; }

  .brand {
    position: absolute; left: 46px; top: 100px;
    font-family: "Nunito", sans-serif; font-weight: 700;
    color: var(--ink-white);
  }
  .brand__tagline { font-size: 8.5px; letter-spacing: 0.1px; margin-left: 6px; }
  .brand__mark { display: flex; align-items: center; gap: 6px; margin-top: 3px; }
  .brand__dot { width: 14px; height: 14px; border-radius: 50%; background: var(--band-colour); }
  .brand__name { font-size: 18px; letter-spacing: 2px; line-height: 1; }

  .snack-photo {
    position: absolute; left: 5px; right: 10px; top: 168px; height: 143px;
    background:
      radial-gradient(circle at 20% 35%, var(--snack-light) 0 12%, transparent 30%),
      radial-gradient(circle at 65% 60%, var(--snack-light) 0 10%, transparent 28%),
      linear-gradient(180deg, var(--snack-mid), var(--snack-deep) 55%, var(--snack-mid));
  }

  .title {
    position: absolute; left: 0; top: 322px; width: 324px; height: 140px;
    color: var(--ink-white);
  }
  .title__top {
    position: absolute; left: 80px; top: 0;
    font-family: "Bebas Neue", sans-serif; font-size: 56px; line-height: 1;
    letter-spacing: 0.5px;
  }
  .title__script {
    position: absolute; left: 68px; top: 30px;
    font-family: "Allura", cursive; font-size: 84px; line-height: 1;
    color: var(--script-colour);
  }
  .title__bottom {
    position: absolute; left: 108px; top: 74px;
    font-family: "Bebas Neue", sans-serif; font-size: 72px; line-height: 1;
    letter-spacing: 9px;
  }

  .net-weight {
    position: absolute; left: 23px; width: 280px; top: 484px; height: 17px;
    background: var(--band-colour);
    font-family: "Libre Baskerville", serif; font-size: 9.5px;
    color: var(--band-text);
    display: flex; align-items: center; justify-content: center;
  }
</style>
</head>
<body>
<main class="sheet">

  <section class="pouch pouch--charcoal">
    <div class="pouch__seal pouch__seal--upper"></div>
    <div class="pouch__seal"></div>
    <div class="brand">
      <p class="brand__tagline">Tiny Wonders bring Rain</p>
      <div class="brand__mark"><span class="brand__dot"></span><span class="brand__name">TWbR</span></div>
    </div>
    <div class="snack-photo" role="img" aria-label="Close-up photograph of golden, crunchy curled snack pieces"></div>
    <h1 class="title">
      <span class="title__top">LANTERN</span>
      <span class="title__script">Curl</span>
      <span class="title__bottom">BITES</span>
    </h1>
    <p class="net-weight">NET WT 16OZ (453 Gm)</p>
  </section>

  <section class="pouch pouch--rose">
    <div class="pouch__seal pouch__seal--upper"></div>
    <div class="pouch__seal"></div>
    <div class="brand">
      <p class="brand__tagline">Tiny Wonders bring Rain</p>
      <div class="brand__mark"><span class="brand__dot"></span><span class="brand__name">TWbR</span></div>
    </div>
    <div class="snack-photo" role="img" aria-label="Close-up photograph of golden, crunchy curled snack pieces"></div>
    <h2 class="title">
      <span class="title__top">LANTERN</span>
      <span class="title__script">Curl</span>
      <span class="title__bottom">BITES</span>
    </h2>
    <p class="net-weight">NET WT 16OZ (453 Gm)</p>
  </section>

  <section class="pouch pouch--forest">
    <div class="pouch__seal pouch__seal--upper"></div>
    <div class="pouch__seal"></div>
    <div class="brand">
      <p class="brand__tagline">Tiny Wonders bring Rain</p>
      <div class="brand__mark"><span class="brand__dot"></span><span class="brand__name">TWbR</span></div>
    </div>
    <div class="snack-photo" role="img" aria-label="Close-up photograph of golden, crunchy curled snack pieces"></div>
    <h2 class="title">
      <span class="title__top">LANTERN</span>
      <span class="title__script">Curl</span>
      <span class="title__bottom">BITES</span>
    </h2>
    <p class="net-weight">NET WT 16OZ (453 Gm)</p>
  </section>

  <section class="pouch pouch--stone">
    <div class="pouch__seal pouch__seal--upper"></div>
    <div class="pouch__seal"></div>
    <div class="brand">
      <p class="brand__tagline">Tiny Wonders bring Rain</p>
      <div class="brand__mark"><span class="brand__dot"></span><span class="brand__name">TWbR</span></div>
    </div>
    <div class="snack-photo" role="img" aria-label="Close-up photograph of golden, crunchy curled snack pieces"></div>
    <h2 class="title">
      <span class="title__top">LANTERN</span>
      <span class="title__script">Curl</span>
      <span class="title__bottom">BITES</span>
    </h2>
    <p class="net-weight">NET WT 16OZ (453 Gm)</p>
  </section>

</main>
</body>
</html>
```